RTV Engineering Business Card Design

We’re looking for an elegant, clean, and timeless business card design that communicates experience, capability, and reliability.

RTV Engineering was established in 1995 , we are a Government Contracting company providing Professional Services to the Department of Harbor Affairs, Frontier Resilience and the Signals Consortium. Our capabilities include: Acquisition & Program Management; Intelligence & Security Operations; Cyber, IT & Network Operations; Lifecycle Logistics & Asset Readiness; C5ISR Systems Engineering & Sustainment.

We want the card to reflect a straightforward, confident approach to business. The design should feel polished and professional without being flashy or overly corporate.

Design Direction
Clean, sophisticated, and uncluttered
Elegant but understated
Strong typography and thoughtful spacing
A timeless aesthetic rather than something overly trendy
Confident and established, with a sense of substance
Easy to read and practical in a real-world business setting

The overall impression should be: “These are experienced professionals who know what they’re doing, do what they say, and can be relied upon.”

We’re open to creative interpretations. The finished card should feel distinctive through its typography, proportions, layout, and attention to detail rather than through excessive graphics or visual effects.

We’re looking for a design that would make a potential client immediately feel that they’re dealing with a capable, trustworthy, and established company.

Company Colors: Navy and Gold/Yellow (but you do not need to use these colors on the card)
Company Name: RTV Engineering Associates, Inc. (known as RTV Engineering)
Website: rtvengineering-hq.example
Company Logo: Navy & Gold (other variations attached)

```html
<!DOCTYPE html>
<html lang="en">
<head>
<meta charset="utf-8">
<title>RTV Engineering Business Card</title>
<link rel="stylesheet" href="https://fonts.googleapis.com/css2?family=Figtree:wght@400;500;600;700;800&family=Barlow:wght@500;600&display=swap">
<style>
  :root {
    --navy: #1b2742;
    --ink-navy: #1f2a5c;
    --gold: #c9a23a;
    --gold-line: #c79f2e;
    --muted: #6a7597;
    --paper: #efefef;
    --stage: #d3d3d3;
    --white: #ffffff;
    --text: #1a1a1a;
  }
  * { margin: 0; padding: 0; box-sizing: border-box; }
  html, body { width: 1200px; height: 1200px; overflow: hidden; }
  body { background: var(--stage); position: relative; font-family: "Figtree", sans-serif; }

  .card { position: absolute; left: 180px; width: 840px; height: 480px; overflow: hidden; }
  .card--front { top: 78px; background: var(--paper); }
  .card--back { top: 630px; background: var(--navy); }

  /* Front: navy brand panel */
  .brand-panel { position: absolute; left: 0; top: 0; width: 377px; height: 480px; background: var(--navy); }
  .wordmark { position: absolute; font-family: "Figtree", sans-serif; font-weight: 800; color: var(--white); letter-spacing: 0.01em; line-height: 1; }
  .brand-panel .wordmark { left: 0; width: 377px; text-align: center; top: 140px; font-size: 70px; }
  .brand-panel .company { position: absolute; left: 68px; top: 274px; font-family: "Barlow", sans-serif; font-weight: 600; font-size: 16px; line-height: 20px; letter-spacing: 0.36em; color: var(--muted); }
  .brand-panel .established { position: absolute; left: 68px; top: 378px; font-family: "Barlow", sans-serif; font-weight: 600; font-size: 17px; line-height: 20px; letter-spacing: 0.08em; color: var(--muted); }
  .established .year { color: var(--gold); }
  .est-rule { position: absolute; left: 196px; top: 388px; width: 582px; height: 1px; background: var(--gold-line); }

  /* Front: contact side */
  .person-name { position: absolute; left: 432px; top: 76px; font-weight: 700; font-size: 38px; line-height: 44px; color: var(--ink-navy); letter-spacing: -0.005em; white-space: nowrap; }
  .person-role { position: absolute; left: 432px; top: 126px; font-weight: 500; font-size: 19px; line-height: 24px; color: var(--gold); white-space: nowrap; }
  .name-rule { position: absolute; left: 432px; top: 164px; width: 346px; height: 1px; background: var(--gold-line); }

  .contact { position: absolute; left: 436px; list-style: none; }
  .contact li { position: relative; padding-left: 36px; font-weight: 500; font-size: 21px; line-height: 25.5px; color: var(--text); white-space: nowrap; }
  .contact svg { position: absolute; left: 0; top: 2px; width: 22px; height: 22px; fill: none; stroke: var(--gold); stroke-width: 1.4; stroke-linecap: round; stroke-linejoin: round; }
  .contact--phone { top: 191px; }
  .contact--address { top: 235px; }
  .contact--web { top: 331px; }

  .front-tagline { position: absolute; left: 432px; top: 398px; font-family: "Barlow", sans-serif; font-weight: 600; font-size: 16px; line-height: 20px; letter-spacing: 0.1em; color: var(--ink-navy); white-space: nowrap; }

  /* Back */
  .card--back .wordmark { left: 0; width: 840px; text-align: center; top: 130px; font-size: 96px; }
  .back-company { position: absolute; left: 0; width: 840px; top: 256px; text-align: center; font-family: "Barlow", sans-serif; font-weight: 600; font-size: 17px; letter-spacing: 0.32em; color: var(--white); }
  .back-est { position: absolute; left: 93px; width: 654px; top: 323px; display: flex; align-items: center; gap: 12px; }
  .back-est .rule { flex: 1; height: 1px; background: var(--gold-line); }
  .back-est span { font-family: "Barlow", sans-serif; font-weight: 600; font-size: 16px; letter-spacing: 0.3em; color: var(--white); }
  .back-tagline { position: absolute; left: 0; width: 840px; top: 387px; text-align: center; font-family: "Barlow", sans-serif; font-weight: 500; font-size: 23px; letter-spacing: 0.09em; color: var(--gold); }
</style>
</head>
<body>

<section class="card card--front" aria-label="Business card front">
  <div class="brand-panel">
    <div class="wordmark">RTV</div>
    <div class="company">RTV ENGINEERING<br>ASSOCIATES, INC.</div>
    <div class="established">ESTABLISHED<br><span class="year">IN 1995</span></div>
  </div>
  <div class="est-rule"></div>

  <div class="person-name">Marla Venturini</div>
  <div class="person-role">President, CEO &amp; Founder</div>
  <div class="name-rule"></div>

  <ul class="contact contact--phone">
    <li>
      <svg viewBox="0 0 24 24" aria-hidden="true"><path d="M5 3.5l3 .5 1.5 4-2 1.5c1 2.5 3 4.5 5.5 5.5l1.5-2 4 1.5.5 3c-.5 1.5-2 2.5-3.5 2.5C9.5 20 4 14.5 4 7.5 4 6 4 4.5 5 3.5z"/><path d="M14 4a6 6 0 0 1 6 6M14 7.5a2.5 2.5 0 0 1 2.5 2.5"/></svg>
      555-014-2280
    </li>
  </ul>
  <ul class="contact contact--address">
    <li>
      <svg viewBox="0 0 24 24" aria-hidden="true"><path d="M3 21h18M5 21V4h8v17M13 9h6v12M8 8h2M8 11h2M8 14h2M8 17h2M15.5 13h1.5M15.5 16h1.5"/></svg>
      4120 Harborline Avenue,<br>Suite 310, Port Alder,<br>VA 20999
    </li>
  </ul>
  <ul class="contact contact--web">
    <li>
      <svg viewBox="0 0 24 24" aria-hidden="true"><circle cx="12" cy="12" r="9"/><path d="M3 12h18M12 3c2.5 2.5 3.5 5.5 3.5 9s-1 6.5-3.5 9c-2.5-2.5-3.5-5.5-3.5-9s1-6.5 3.5-9z"/></svg>
      rtvengineering-hq.example
    </li>
  </ul>

  <div class="front-tagline">EXPERIENCE. CAPABILITY. RELIABILITY.</div>
</section>

<section class="card card--back" aria-label="Business card back">
  <div class="wordmark">RTV</div>
  <div class="back-company">RTV ENGINEERING ASSOCIATES, INC.</div>
  <div class="back-est"><div class="rule"></div><span>ESTABLISHED 1995</span><div class="rule"></div></div>
  <div class="back-tagline">Professional Services for Defense, Security &amp; Intelligence</div>
</section>

</body>
</html>
```